New Company Business Card Design

I have a new company logo and I want a new business card design. I dont know if the logo file i attached is in the correct format or quality. We are a New York City Specialty construction Firm specializing in high risk out of the box projects. I want a simple and classy business card that people will his card is as crisp as the work his company does.

Target Market(s)

Clients in the heavy construction industry in New York City

Industry/Entity Type

Construction Company

Contact Information for Business Card

Simple Classy - DIFFERENT

Font styles to use
Other font styles liked:
• Mach the logo font in some way

Colors

Designer to choose colors to be used in the design.

Requirements
Must have
• Uniqueness
Nice to have
• Nothing particular - Just different and classy - Timeless
Should not have
• Goofy Shit or Gimmicky shit

```html
<!DOCTYPE html>
<html lang="en">
<head>
<meta charset="utf-8">
<title>Halden Works, Inc. — Business Card</title>
<link rel="stylesheet" href="https://fonts.googleapis.com/css2?family=Roboto:wght@400;500;700;900&display=swap">
<style>
  :root {
    --backdrop: #e3e3e3;
    --card-white: #f7f7f7;
    --brand-blue: #0b58a3;
    --brand-blue-deep: #07468a;
    --brand-blue-light: #1ea0dc;
    --ink: #111111;
    --text-grey: #4a4a4a;
    --divider: #b9b9b9;
  }
  html, body {
    margin: 0;
    padding: 0;
    width: 1200px;
    height: 960px;
    overflow: hidden;
    background: var(--backdrop);
    font-family: "Roboto", Arial, sans-serif;
  }
  .canvas {
    position: relative;
    width: 1200px;
    height: 960px;
  }
  .card {
    position: absolute;
    width: 600px;
    height: 343px;
    box-sizing: border-box;
  }

  /* Front */
  .card-front {
    left: 314px;
    top: 113px;
    background: var(--card-white);
    overflow: hidden;
  }
  .front-brand {
    position: absolute;
    left: 40px;
    top: 0;
    width: 290px;
    height: 330px;
    display: flex;
    align-items: center;
    justify-content: center;
    gap: 10px;
  }
  .brand-square {
    width: 18px;
    height: 18px;
    background: var(--brand-blue);
  }
  .brand-name {
    font-weight: 700;
    font-size: 27px;
    letter-spacing: 1px;
    color: var(--brand-blue);
    text-transform: uppercase;
  }
  .front-divider {
    position: absolute;
    left: 328px;
    top: 77px;
    width: 1px;
    height: 195px;
    background: var(--divider);
  }
  .contact-block {
    position: absolute;
    left: 353px;
    top: 72px;
  }
  .person-name {
    margin: 0;
    font-weight: 700;
    font-size: 21px;
    line-height: 24px;
    color: var(--brand-blue);
    letter-spacing: 0.3px;
  }
  .person-title {
    margin: 0 0 19px;
    font-weight: 500;
    font-size: 14px;
    line-height: 18px;
    color: var(--ink);
  }
  .address {
    margin: 0 0 9px;
    font-size: 14px;
    line-height: 19px;
    color: var(--text-grey);
  }
  .contact-list {
    list-style: none;
    margin: 0;
    padding: 0;
  }
  .contact-list li {
    display: flex;
    align-items: center;
    height: 19px;
    font-size: 14px;
    color: var(--text-grey);
  }
  .contact-icon {
    width: 13px;
    height: 13px;
    margin-right: 10px;
    fill: var(--brand-blue);
    flex: none;
  }
  .front-band {
    position: absolute;
    left: 0;
    bottom: 0;
    width: 600px;
    height: 12px;
  }

  /* Back */
  .card-back {
    left: 311px;
    top: 472px;
    background: radial-gradient(ellipse 55% 70% at 50% 45%, var(--brand-blue-light) 0%, #137cc4 45%, var(--brand-blue-deep) 100%);
  }
  .back-brand {
    position: absolute;
    left: 0;
    top: 130px;
    width: 600px;
    display: flex;
    align-items: center;
    justify-content: center;
    gap: 14px;
  }
  .back-brand .brand-square {
    width: 24px;
    height: 24px;
    background: #ffffff;
  }
  .back-brand .brand-name {
    font-size: 40px;
    color: #ffffff;
  }
  .back-web {
    position: absolute;
    left: 0;
    top: 288px;
    width: 600px;
    text-align: center;
    font-size: 14px;
    letter-spacing: 5px;
    color: #e8f3fb;
  }
</style>
</head>
<body>
<main class="canvas">

  <section class="card card-front" aria-label="Business card front">
    <div class="front-brand">
      <span class="brand-square"></span>
      <span class="brand-name">Halden Works</span>
    </div>

    <div class="front-divider"></div>

    <div class="contact-block">
      <h1 class="person-name">DANIEL REYES</h1>
      <p class="person-title">CEO/FOUNDER</p>
      <p class="address">2140 Harbor Street<br>Brooklyn, New York 11201</p>
      <ul class="contact-list">
        <li>
          <svg class="contact-icon" viewBox="0 0 16 16" aria-hidden="true"><path d="M3.6 1l2.6 2.6-1.5 2a9 9 0 0 0 5.7 5.7l2-1.5L15 12.4 13.4 15C6.9 15 1 9.1 1 2.6z"/></svg>
          718 555 0142
        </li>
        <li>
          <svg class="contact-icon" viewBox="0 0 16 16" aria-hidden="true"><path d="M4 0h8a1 1 0 0 1 1 1v14a1 1 0 0 1-1 1H4a1 1 0 0 1-1-1V1a1 1 0 0 1 1-1zm1 2v10h6V2zm3 11a1 1 0 1 0 0 2 1 1 0 0 0 0-2z"/></svg>
          917 555 0187
        </li>
        <li>
          <svg class="contact-icon" viewBox="0 0 16 16" aria-hidden="true"><path d="M4 0h7l2 2v4H4zM1 7h14v6h-2v-2H3v2H1zm3 5h8v4H4z"/></svg>
          718 555 0163
        </li>
        <li>
          <svg class="contact-icon" viewBox="0 0 16 16" aria-hidden="true"><path d="M1 3h14v10H1zm1.5 1.3V5l5.5 4 5.5-4v-.7L8 8.2z"/></svg>
          daniel@haldenworks.com
        </li>
        <li>
          <svg class="contact-icon" viewBox="0 0 16 16" aria-hidden="true"><path d="M8 1a7 7 0 1 0 0 14A7 7 0 0 0 8 1zm-1 2.2c-.6.8-.5 1.6.4 2 .8.4.7 1.2 0 1.6-.9.5-2.2 0-2.8 1-.5.8.1 1.9-.2 2.8-.2.7-.8.9-1.3.8A5.5 5.5 0 0 1 7 3.2zm2.2 9.6c.2-1 1-1.6 1.8-2.3.6-.5.7-1.4.1-1.9-.6-.4-1.5-.2-1.9-.9-.3-.6.3-1.3 1-1.4.9-.1 1.8-.6 1.9-1.2a5.5 5.5 0 0 1-2.9 7.7z"/></svg>
          www.haldenworks.com
        </li>
      </ul>
    </div>

    <svg class="front-band" viewBox="0 0 600 12" preserveAspectRatio="none" aria-hidden="true">
      <defs>
        <linearGradient id="band-blue" x1="0" x2="1" y1="0" y2="0">
          <stop offset="0" stop-color="#0a4f9a"/>
          <stop offset="0.55" stop-color="#1e9ad8"/>
          <stop offset="1" stop-color="#0a4f9a"/>
        </linearGradient>
      </defs>
      <polygon points="0,0 394,0 391,12 0,12" fill="url(#band-blue)"/>
      <polygon points="394,0 397,0 394,12 391,12" fill="#ffffff"/>
      <polygon points="397,0 600,0 600,12 394,12" fill="#0a0a0a"/>
    </svg>
  </section>

  <section class="card card-back" aria-label="Business card back">
    <div class="back-brand">
      <span class="brand-square"></span>
      <span class="brand-name">Halden Works</span>
    </div>
    <p class="back-web">www.haldenworks.com</p>
  </section>

</main>
</body>
</html>
```